Business card design for engineering firm specializing in defense industry.

We need a professional business card design. Something simple but stands out. We are an engineering company specializing in composites in the defense industry.
Industry/Entity Type
Defense
Contact Information for Business Card
A simple black business card with the Varlonix yellow color is what we had in mind but open for other designs.
Colors
ffc214

```html
<!DOCTYPE html>
<html lang="en">
<head>
<meta charset="utf-8">
<title>Varlonix Business Card</title>
<link rel="stylesheet" href="https://fonts.googleapis.com/css2?family=Open+Sans:wght@400;600;700&display=swap">
<style>
  :root {
    --page-bg: #f4f4f4;
    --card-dark: #231f20;
    --card-light: #ffffff;
    --brand-yellow: #ffc214;
    --ink: #2b2b2b;
    --ink-soft: #333333;
    --mark-grey: #4a4e54;
  }
  * { margin: 0; padding: 0; box-sizing: border-box; }
  html, body {
    width: 1200px;
    height: 900px;
    overflow: hidden;
    background: var(--page-bg);
    font-family: "Open Sans", Arial, sans-serif;
  }
  .canvas { position: relative; width: 1200px; height: 900px; }

  .card {
    position: absolute;
    left: 306px;
    width: 588px;
    height: 336px;
  }
  .card--front { top: 98px; background: var(--card-dark); }
  .card--back { top: 465px; background: var(--card-light); }

  .front-wordmark {
    position: absolute;
    left: 0; right: 0;
    top: 128px;
    text-align: center;
    font-weight: 700;
    font-size: 54px;
    line-height: 1;
    color: var(--mark-grey);
    letter-spacing: 1px;
  }

  .back-logo {
    position: absolute;
    left: 56px;
    top: 140px;
    display: flex;
    align-items: center;
    gap: 10px;
  }
  .back-logo__square {
    width: 22px;
    height: 22px;
    background: var(--brand-yellow);
  }
  .back-logo__name {
    font-weight: 700;
    font-size: 30px;
    line-height: 1;
    color: var(--ink);
  }

  .contact {
    position: absolute;
    left: 328px;
    top: 79px;
    color: var(--ink-soft);
  }
  .contact__name {
    font-weight: 600;
    font-size: 18px;
    letter-spacing: 0.3px;
    line-height: 22px;
    color: var(--ink);
  }
  .contact__role {
    font-size: 13px;
    line-height: 18px;
    color: var(--brand-yellow);
  }
  .contact__address {
    margin-top: 14px;
    font-size: 15px;
    line-height: 21px;
  }
  .contact__list {
    list-style: none;
    margin-top: 11px;
  }
  .contact__item {
    display: flex;
    align-items: center;
    gap: 10px;
    font-size: 15px;
    line-height: 24px;
  }
  .contact__icon { width: 18px; height: 18px; flex: none; }
</style>
</head>
<body>
<main class="canvas">
  <section class="card card--front" aria-label="Card front">
    <div class="front-wordmark">Varlonix</div>
  </section>

  <section class="card card--back" aria-label="Card back">
    <div class="back-logo">
      <span class="back-logo__square"></span>
      <span class="back-logo__name">Varlonix</span>
    </div>

    <div class="contact">
      <h1 class="contact__name">DANIEL WHITFORD</h1>
      <p class="contact__role">Founder | CEO</p>
      <p class="contact__address">214 Harlow Ridge Lane,<br>Brenton Falls 40218, NC</p>
      <ul class="contact__list">
        <li class="contact__item">
          <svg class="contact__icon" viewBox="0 0 24 24" aria-hidden="true"><path fill="#ffc214" d="M6.6 10.8a15.1 15.1 0 0 0 6.6 6.6l2.2-2.2a1 1 0 0 1 1-.25 11.4 11.4 0 0 0 3.6.57 1 1 0 0 1 1 1V20a1 1 0 0 1-1 1A17 17 0 0 1 3 4a1 1 0 0 1 1-1h3.5a1 1 0 0 1 1 1c0 1.25.2 2.45.57 3.57a1 1 0 0 1-.25 1z"/></svg>
          <span>0412 555 019</span>
        </li>
        <li class="contact__item">
          <svg class="contact__icon" viewBox="0 0 24 24" aria-hidden="true"><rect x="2" y="5" width="20" height="14" fill="#ffc214"/><path d="M2.5 5.5 12 13l9.5-7.5" fill="none" stroke="#fff" stroke-width="1.6"/></svg>
          <span>info@yourdomain.com</span>
        </li>
        <li class="contact__item">
          <svg class="contact__icon" viewBox="0 0 24 24" aria-hidden="true"><circle cx="12" cy="12" r="10" fill="#ffc214"/><path d="M7 7c2 1 3 0 4 2s-1 3 1 4 1 4 0 5M15 4c0 2 2 2 3 3s-1 3 1 4" fill="none" stroke="#fff" stroke-width="1.6"/></svg>
          <span>www.yourdomain.com</span>
        </li>
      </ul>
    </div>
  </section>
</main>
</body>
</html>
```